Need creative website for award-winning author

I need someone to create a cool website for indie award-winning author Lorna Quibble. Right now she one young adult novel and a published short story. The site should appeal to both adults and children. The site has to needs to be available through HOSTWREN's platform.

HOME Page
About Lorna
Bio
Books
Community Projects
Appearances
Blogs & Videos
Contact
Store

Check out the following author's websites:
Paul Drisko
Marla Tubb
Hazel Worf
Gina Falworth
Rina Caldbeck

Target Market(s)

Readers (all ages)

Industry/Entity Type

Adult

Coding

Coded - Design and coding required

Number of Pages Required

5+ page

Requirements
Must have
• Cutting edge look

```html
<!DOCTYPE html>
<html lang="en">
<head>
<meta charset="utf-8">
<title>Lorna Quibble — Author</title>
<link href="https://fonts.googleapis.com/css2?family=Montserrat:wght@400;500&family=Raleway:wght@400;500&display=swap" rel="stylesheet">
<style>
  :root {
    --ink: #2b303b;
    --muted: #6b6f78;
    --accent: #e4141b;
    --white: #ffffff;
    --hero-dark: #1c1c1e;
    --hero-rose: #5a1a32;
    --hero-slate: #3a3d42;
    --cover-top: #3f9ad8;
    --cover-mid: #7fd3ec;
    --cover-bottom: #4a8fd6;
  }
  * { box-sizing: border-box; margin: 0; padding: 0; }
  html, body { width: 1200px; height: 1200px; overflow: hidden; background: var(--white); }
  body { position: relative; font-family: "Raleway", sans-serif; }

  .author-bio {
    position: absolute; left: 0; top: 0; width: 1200px; height: 578px;
    color: var(--white);
  }
  .author-bio__backdrop {
    position: absolute; inset: 0;
    background: linear-gradient(90deg, var(--hero-dark) 0%, var(--hero-rose) 50%, var(--hero-slate) 100%);
  }
  .author-bio__backdrop::after {
    content: ""; position: absolute; inset: 0; background: rgba(0,0,0,0.35);
  }
  .section-title {
    position: absolute; left: 0; width: 1200px; text-align: center;
    font-family: "Montserrat", sans-serif; font-weight: 400;
    font-size: 32px; letter-spacing: 2px; line-height: 1;
  }
  .section-rule {
    position: absolute; left: 510px; width: 180px; height: 2px; background: var(--accent);
  }
  .author-bio .section-title { top: 152px; }
  .author-bio .section-rule { top: 220px; }
  .author-bio__text {
    position: absolute; left: 278px; top: 258px; width: 625px;
    font-size: 14.5px; line-height: 33px; letter-spacing: -0.2px;
  }
  .author-bio__text p + p { margin-top: 17px; }

  .recent-publishes .section-title { top: 657px; color: var(--ink); }
  .recent-publishes .section-rule { top: 725px; }
  .recent-publishes__lead {
    position: absolute; left: 0; top: 767px; width: 1200px; text-align: center;
    font-size: 21px; color: var(--muted);
  }
  .book-cover {
    position: absolute; top: 853px; width: 226px; height: 347px;
    background: linear-gradient(180deg, var(--cover-top) 0%, var(--cover-mid) 55%, var(--cover-bottom) 100%);
  }
</style>
</head>
<body>
  <section class="author-bio">
    <div class="author-bio__backdrop" role="img" aria-label="Darkened photo of the author with a friend at a book fair booth"></div>
    <h2 class="section-title">AUTHOR BIO</h2>
    <div class="section-rule"></div>
    <div class="author-bio__text">
      <p>Lorna Quibble spent most of her adult life working on projects that empower youth to achieve their dreams.</p>
      <p>Bright Feathers, inspired by volunteerism on her daughter's neighborhood swim team, is a creative extension of her work as a community planner.</p>
      <p>She currently lives with her husband, two daughters and three dogs in Valencia, California, where she co-owns a community planning firm.</p>
    </div>
  </section>

  <section class="recent-publishes">
    <h2 class="section-title">RECENT PUBLISHES</h2>
    <div class="section-rule"></div>
    <p class="recent-publishes__lead">Lorem ipsum dolor sit amet, consectetur adipiscing elit.</p>
    <div class="book-cover" style="left:107px" role="img" aria-label="Book cover of Bright Feathers by Lorna Quibble"></div>
    <div class="book-cover" style="left:361px" role="img" aria-label="Book cover of Bright Feathers by Lorna Quibble"></div>
    <div class="book-cover" style="left:614px" role="img" aria-label="Book cover of Bright Feathers by Lorna Quibble"></div>
    <div class="book-cover" style="left:867px" role="img" aria-label="Book cover of Bright Feathers by Lorna Quibble"></div>
  </section>
</body>
</html>
```